We are looking to design a black on white bourbon label for a new brand
in att we have added
1. the bottle we need to use (wine bottle in black)
2. some industry examples (Look at horse rider label good example of where we need to go)
3. horses and cowboys illistrations

The brand will be Called OLD BRASS LANTERN. we want an old school feeling label prohibition style.

What we need on the label is
1. visual = Bucking Horse + rider cowboy + lasso forming a circle
2. Name = Old Brass Lantern Bourbon Straight Aged Whiskey
3. Product info = 70 CL 40 ABV
4. Distilled in the Wild Wild West WWW.OLDBRASSLANTERNSPIRITS.COM

```html
<!DOCTYPE html>
<html lang="en">
<head>
<meta charset="utf-8">
<title>Old Brass Lantern Bourbon – Label and Wordmark</title>
<link rel="stylesheet" href="https://fonts.googleapis.com/css2?family=Oswald:wght@500;600&family=Rye&display=swap">
<style>
  :root {
    --backdrop: #1d1d1f;
    --backdrop-glow: #3a3a3c;
    --label-paper: #fbfbf8;
    --label-rule: #b9865a;
    --bourbon-brown: #6a3a1c;
    --ink: #2a2624;
    --cream: #ece4cf;
    --art-light: #d9d7d4;
    --art-dark: #6d6966;
  }
  * { margin: 0; padding: 0; box-sizing: border-box; }
  html, body { width: 1200px; height: 1082px; overflow: hidden; }
  body {
    background: radial-gradient(ellipse at 50% 20%, var(--backdrop-glow) 0%, var(--backdrop) 60%);
    font-family: "Oswald", "Arial Narrow", sans-serif;
    position: relative;
  }
  .label {
    position: absolute;
    left: 190px;
    top: 211px;
    width: 360px;
    height: 660px;
  }
  .label text { font-family: "Oswald", "Arial Narrow", sans-serif; }
  .label .display { font-family: "Rye", "Georgia", serif; font-weight: 400; }
  .wordmark {
    position: absolute;
    left: 640px;
    top: 410px;
    width: 420px;
    text-align: center;
    color: var(--cream);
  }
  .wordmark-name {
    font-family: "Rye", "Georgia", serif;
    font-weight: 400;
    font-size: 46px;
    line-height: 1.15;
    letter-spacing: 1px;
  }
  .wordmark-tagline {
    margin-top: 14px;
    font-weight: 500;
    font-size: 19px;
    letter-spacing: 2.5px;
  }
</style>
</head>
<body>

<svg class="label" viewBox="0 0 360 660" xmlns="http://www.w3.org/2000/svg" aria-label="Old Brass Lantern Bourbon label">
  <defs>
    <path id="arc-top" d="M40,92 Q180,20 320,92"/>
    <path id="arc-bottom" d="M52,590 Q180,644 308,590"/>
    <linearGradient id="art-tone" x1="0" y1="0" x2="0" y2="1">
      <stop offset="0" stop-color="var(--art-light)"/>
      <stop offset="0.55" stop-color="var(--art-dark)"/>
      <stop offset="1" stop-color="var(--art-light)"/>
    </linearGradient>
  </defs>

  <path class="label-shape" d="M6,70 Q6,52 24,44 Q180,-14 336,44 Q354,52 354,70 L354,588 Q354,606 336,614 Q180,672 24,614 Q6,606 6,588 Z" fill="var(--label-paper)"/>
  <path class="label-border" d="M14,74 Q14,58 30,51 Q180,-3 330,51 Q346,58 346,74 L346,584 Q346,600 330,607 Q180,661 30,607 Q14,600 14,584 Z" fill="none" stroke="var(--label-rule)" stroke-width="1.2"/>

  <text font-size="15" font-weight="500" fill="var(--ink)" letter-spacing="1.6">
    <textPath href="#arc-top" startOffset="50%" text-anchor="middle">BOURBON STRAIGHT AGED WHISKEY</textPath>
  </text>

  <rect class="label-illustration" x="40" y="96" width="280" height="250" rx="6" fill="url(#art-tone)" role="img" aria-label="Engraved illustration of a cowboy on a bucking horse swinging a lasso that forms a circle"/>

  <g class="label-name" fill="var(--bourbon-brown)" text-anchor="middle">
    <text class="display" x="180" y="406" font-size="38" textLength="270" lengthAdjust="spacingAndGlyphs">OLD BRASS</text>
    <text class="display" x="180" y="456" font-size="38" textLength="240" lengthAdjust="spacingAndGlyphs">LANTERN</text>
  </g>

  <g class="label-style">
    <line x1="58" y1="493" x2="108" y2="493" stroke="var(--bourbon-brown)" stroke-width="1.4"/>
    <line x1="252" y1="493" x2="302" y2="493" stroke="var(--bourbon-brown)" stroke-width="1.4"/>
    <text x="180" y="504" font-size="30" font-weight="600" fill="var(--bourbon-brown)" text-anchor="middle" letter-spacing="2.5">BOURBON</text>
  </g>

  <text class="label-volume" x="180" y="545" font-size="17" font-weight="500" fill="var(--bourbon-brown)" text-anchor="middle" letter-spacing="1.5">70 CL 40 ABV</text>

  <text class="label-web" x="180" y="570" font-size="10" font-weight="500" fill="var(--ink)" text-anchor="middle" letter-spacing="1.2">WWW.OLDBRASSLANTERNSPIRITS.COM</text>

  <text font-size="14" font-weight="500" fill="var(--ink)" letter-spacing="1.4">
    <textPath href="#arc-bottom" startOffset="50%" text-anchor="middle">DISTILLED IN THE WILD WILD WEST</textPath>
  </text>
</svg>

<div class="wordmark">
  <div class="wordmark-name">OLD BRASS<br>LANTERN</div>
  <div class="wordmark-tagline">BOURBON STRAIGHT AGED WHISKEY</div>
</div>

</body>
</html>
```